Packaging design - PROTEIN BALLS

PACKAGING
The packaging is a round carton roll, size: Ø73x180 mm, mockup sample enclosed, The label on the carton roll should have a size of 225x178 mm (width x height)

PRODUCT
Chrunchy, cheesy PROTEIN BALLS (100% pure cheese) with a huge amount of protein (65%), a lot of calcium and very low carbogydrates (3%). Diameter about 1.5 cm.

DESIGN
Since our customers are very sporty people, runner, bodybuilder, etc. The design must fit to this sporty customer segment.

FILES
We need the open data for InDesign with all fonts and pictures. If there are licenses tu buy, we will do it.

SUMMARY
1. SNACK
• Crunchy cheese balls with a diameter of about 1.5cm
• 3 different flavors: "Swiss Alpine Salt", "Provencale" and "Hot Chili"
• High in Protein (65%) and Calcium (2%)
• Low in carbohydrates (3%)

2. PACKAGING
• Carton roll, size: Ø73x180 mm
• Background can be every color, but we think a black one will be high premium.
• Maybe different sports are represented in the background, maybe also cheese
• Be creative
• Label applied, size: 225x178 mm

3. DESIGN
• Product name = (Cheese) PROTEIN BALLS
• 3 different colors for the 3 flavors "Swiss Alpine Salt", "Provencale" and "Hot Chili"
• HighProtein, High Calcium and LowCarb must be pointed out on the front
• Swissness: Swiss made must be pointed out
• fresh and young design, most customers are sporty people, pumper with a strong body awareness

TARGET CUSTOMER
Our main customers are extremely sporty people, who work very hard on their muscles and fitness, most of them are runners, cross fitnesser, bodybuilders, etc We will launch the product in fitness centers, in supplement shops and we are planning to make some stories with sporty influencer.

Serif
Sans Serif

• Cheese, naturalness, healthy, PROTEIN balls, muscles, Swissness must showed on the product.

```html
<!DOCTYPE html>
<html lang="en">
<head>
<meta charset="utf-8">
<title>Cheesy Protein Balls – Label</title>
<link rel="stylesheet" href="https://fonts.googleapis.com/css2?family=Exo+2:ital,wght@1,900&family=Saira+Condensed:wght@700;800&family=Fira+Sans+Condensed:wght@500;600&family=Montserrat:wght@400&display=swap">
<style>
  :root {
    --backdrop: #ffffff;
    --kraft: #b49b79;
    --kraft-light: #c2a985;
    --kraft-dark: #a58b68;
    --band: #3b3531;
    --ink: #2d2925;
    --snack-light: #a9803f;
    --snack-dark: #7c5a2a;
  }
  * { margin: 0; padding: 0; box-sizing: border-box; }
  html, body {
    width: 1176px; height: 1200px; overflow: hidden;
    background: var(--backdrop);
  }
  .canvas { position: relative; width: 1176px; height: 1200px; }
  .label {
    position: absolute; top: 125px; height: 910px;
    background: radial-gradient(ellipse at 50% 45%, var(--kraft-light), var(--kraft) 60%, var(--kraft-dark));
  }
  .label--back { left: 176px; width: 306px; }
  .label--front { left: 690px; width: 310px; }

  .back-title {
    position: absolute; top: 104px; left: 0; width: 100%;
    text-align: center; color: var(--ink);
    font-family: "Exo 2", sans-serif; font-style: italic; font-weight: 900;
    line-height: 1.12;
  }
  .back-title .t-small { display: block; font-size: 48px; }
  .back-title .t-big { display: block; font-size: 52px; letter-spacing: 1px; }

  .swiss-made {
    position: absolute; top: 300px; left: 0; width: 100%;
    display: flex; justify-content: center; align-items: center; gap: 8px;
    font-family: "Fira Sans Condensed", sans-serif; font-weight: 600;
    font-size: 16px; letter-spacing: 1.5px; text-transform: uppercase;
    color: var(--ink);
  }
  .swiss-made .mark { width: 12px; height: 12px; background: var(--band); }

  .back-copy {
    position: absolute; top: 350px; left: 41px; width: 226px;
    font-family: "Montserrat", sans-serif; font-size: 11.8px; line-height: 18.6px;
    color: var(--ink); text-align: justify; text-align-last: center; hyphens: auto;
  }
  .sport-photo {
    position: absolute; top: 790px; left: 41px; width: 226px; height: 90px;
    border-radius: 6px;
    background: linear-gradient(90deg, rgba(59,53,49,0.10), rgba(59,53,49,0.28), rgba(59,53,49,0.10));
  }

  .front-art { position: absolute; inset: 0; }
  .flavor {
    position: absolute; top: 760px; left: 0; width: 100%; text-align: center;
    font-family: "Fira Sans Condensed", sans-serif; font-weight: 600;
    font-size: 25px; color: var(--ink);
  }
  .claims {
    position: absolute; top: 808px; left: 0; width: 100%; text-align: center;
    font-family: "Fira Sans Condensed", sans-serif; font-weight: 500;
    font-size: 14px; line-height: 19.5px; color: var(--ink);
  }
  .foot-tab {
    position: absolute; bottom: 0; left: 78px; width: 153px; height: 18px;
    background: var(--band);
  }
</style>
</head>
<body>
<div class="canvas">
  <section class="label label--back">
    <h1 class="back-title">
      <span class="t-small">Cheesy</span>
      <span class="t-big">PROTEIN</span>
      <span class="t-small">balls</span>
    </h1>
    <p class="swiss-made"><span class="mark"></span>Swiss made</p>
    <p class="back-copy">Crunchy, cheesy and made from 100% pure cheese: our protein balls are baked until golden and light, with a diameter of about 1.5cm. Each handful delivers a huge amount of protein (65%), a good dose of calcium (2%) and very low carbohydrates (3%). Made for runners, bodybuilders and cross fitness athletes who work hard on their muscles every single day. Enjoy them after training, on the trail or between meals as a clean, savoury snack without added sugar. Ideal in the gym bag, at the office or on the road, they are an honest reward for every rep, every kilometre and every personal best. Seasoned with Swiss Alpine Salt and produced in Switzerland with care, quality and tradition. Store in a cool, dry place and close the roll well after opening to keep every ball fresh and crunchy.</p>
    <div class="sport-photo" role="img" aria-label="Sports scene with a runner, a weightlifter and a cross fitness athlete"></div>
  </section>

  <section class="label label--front">
    <svg class="front-art" width="310" height="910" viewBox="0 0 310 910">
      <defs>
        <linearGradient id="snack-tone" x1="0" y1="0" x2="1" y2="0">
          <stop offset="0" stop-color="var(--snack-dark)" stop-opacity="0.55"/>
          <stop offset="0.5" stop-color="var(--snack-light)" stop-opacity="0.75"/>
          <stop offset="1" stop-color="var(--snack-dark)" stop-opacity="0.55"/>
        </linearGradient>
      </defs>
      <rect class="snack-photo" role="img" aria-label="Stacked column of crunchy cheese protein balls" x="4" y="43" width="74" height="686" rx="30" fill="url(#snack-tone)"/>
      <rect class="snack-photo" role="img" aria-label="Stacked column of crunchy cheese protein balls" x="228" y="43" width="78" height="686" rx="30" fill="url(#snack-tone)"/>
      <polygon class="name-band" points="78,0 231,0 231,690 78,710" fill="var(--band)"/>
      <text class="product-name" transform="translate(161 674) rotate(-90)" font-family="Saira Condensed, sans-serif" font-weight="800" font-size="74" fill="var(--kraft)" textLength="619" lengthAdjust="spacingAndGlyphs">Cheesy PROTEIN</text>
      <text class="product-sub" transform="translate(200 658) rotate(-90)" font-family="Saira Condensed, sans-serif" font-weight="700" font-size="31" fill="var(--kraft)" textLength="584" lengthAdjust="spacingAndGlyphs">Balls with a diameter of about 1.5cm</text>
    </svg>
    <h2 class="flavor">Swiss Alpine Salt</h2>
    <p class="claims">High in Protein (65%)<br>Calcium (2%)<br>Low in carbohydrates (3%)</p>
    <div class="foot-tab"></div>
  </section>
</div>
</body>
</html>
```